Marlene Business Card

My wife is going to start her own business with renting holiday appartments to tourists. She needs a design for a new business card... and a new web site.
Look at Roomvesta "Ruhezeit am Birkenteich"

Target Market(s)

Give business card to prospects at any situation

Contact Information for Business Card

not sure what this means

Font styles to use
Script

Colors
fec41a
fee18a

Requirements
Must have
• My wife's handwriting is difficult to read:
Entspannen - Loslassen - Auftanken
Marlene & der Birkenteich
Urlaub an einem besonderen Ort
Marlene Brökel
Gartenpfad 7
17489 Alt Medow
info@marlene-broekel.de
www.birkenteich.net
Nice to have
• Beige background
Font like handwriting

```html
<!DOCTYPE html>
<html lang="de">
<head>
<meta charset="utf-8">
<title>Marlene &amp; der Birkenteich – Visitenkarte</title>
<link rel="stylesheet" href="https://fonts.googleapis.com/css2?family=Yesteryear&family=EB+Garamond&family=Jost:wght@500;600&display=swap">
<style>
  :root {
    --backdrop: #8e8e8e;
    --paper: #ecebdf;
    --ink: #2a2b33;
    --url: #d9d9d6;
  }
  html, body {
    margin: 0;
    width: 1200px;
    height: 904px;
    overflow: hidden;
    background: var(--backdrop);
  }
  .card {
    position: absolute;
    left: 100px;
    top: 172px;
    width: 1000px;
    height: 560px;
    background: var(--paper);
    overflow: hidden;
    color: var(--ink);
    box-shadow: 0 10px 30px rgba(0,0,0,.25);
  }
  .card__wave {
    position: absolute;
    inset: 0;
    width: 100%;
    height: 100%;
  }
  .wave__band { fill: var(--ink); }
  .wave__line { fill: none; stroke: var(--ink); stroke-width: 5; stroke-linecap: round; }
  .motto {
    position: absolute;
    left: 170px;
    top: 40px;
    margin: 0;
    font: 58px "Yesteryear", cursive;
    white-space: nowrap;
  }
  .brand {
    position: absolute;
    left: 60px;
    top: 130px;
    margin: 0;
    font: 400 70px "Yesteryear", cursive;
    white-space: nowrap;
  }
  .tagline {
    position: absolute;
    left: 80px;
    top: 210px;
    margin: 0;
    font: 28px "EB Garamond", serif;
  }
  .contact {
    position: absolute;
    left: 80px;
    top: 252px;
    margin: 0;
    font: 600 22px/1.3 "Jost", sans-serif;
    font-style: normal;
  }
  .website {
    position: absolute;
    right: 60px;
    bottom: 56px;
    margin: 0;
    font: 500 32px "Jost", sans-serif;
    letter-spacing: .2em;
    color: var(--url);
  }
</style>
</head>
<body>
  <main class="card">
    <svg class="card__wave" viewBox="0 0 1000 560" preserveAspectRatio="none" aria-hidden="true">
      <path class="wave__band" d="M0,340 C40,420 170,455 380,455 C580,455 770,425 1000,405 L1000,560 L0,560 Z"/>
      <path class="wave__line" d="M0,300 C45,395 175,432 390,434 C480,435 560,432 640,428"/>
    </svg>
    <p class="motto">Entspannen – Loslassen – Auftanken</p>
    <h1 class="brand">Marlene &amp; der Birkenteich</h1>
    <p class="tagline">Urlaub an einem besonderen Ort</p>
    <address class="contact">
      Marlene Brökel,<br>
      Gartenpfad 7, 17489 Alt Medow<br>
      info@marlene-broekel.de
    </address>
    <p class="website">WWW.BIRKENTEICH.NET</p>
  </main>
</body>
</html>
```